Vendora Size Charts - 6 Products

Hi Teodor,

I had you in mind for this, but we have a new e-commerce store that requires the attached 6 size charts re-designed. They are terrible charts from drop shippers and we need them re-designed to match the Palvizo brand logo to designed.

Chart needs to be white background and black letter's. You can add some smart gradients or design to it if you want to make it look elegant and confident.

Can you design 1 chart and we can amend it to perfection with feedback?
Once we agree on the style - you can then do the same style and design for the remaining charts.

Let me know if this is ok?

```html
<!DOCTYPE html>
<html lang="en">
<head>
<meta charset="utf-8">
<title>Size Detail Chart</title>
<link rel="stylesheet" href="https://fonts.googleapis.com/css2?family=Oswald:wght@400;500&display=swap">
<style>
  :root {
    --page-bg: #eceef1;
    --card-bg: #ffffff;
    --frame-red: #c8323f;
    --label-green: #7dc13b;
    --label-green-text: #2f5f0c;
    --ink: #111111;
    --col-size: #fdf0f1;
    --col-bust: #fae3e5;
    --col-length: #f6d3d7;
    --row-rule: #e7a3aa;
    --table-edge: #c8323f;
  }
  * { box-sizing: border-box; margin: 0; padding: 0; }
  html, body {
    width: 1200px;
    height: 1200px;
    overflow: hidden;
    background: var(--page-bg);
  }
  .size-card {
    position: absolute;
    left: 74px;
    top: 220px;
    width: 1052px;
    height: 704px;
    background: var(--card-bg);
    font-family: "Oswald", "Arial Narrow", sans-serif;
    color: var(--ink);
  }
  .frame-lines {
    position: absolute;
    inset: 0;
    width: 100%;
    height: 100%;
  }
  .size-label {
    position: absolute;
    left: 348px;
    top: 40px;
    width: 356px;
    height: 65px;
    background: var(--label-green);
    border-radius: 3px;
    color: var(--label-green-text);
    font-size: 33px;
    font-weight: 500;
    line-height: 65px;
    text-align: center;
  }
  .size-notes {
    position: absolute;
    left: 124px;
    top: 122px;
    width: 806px;
    list-style: none;
    font-size: 19.5px;
    font-weight: 400;
    line-height: 27px;
    letter-spacing: 0.3px;
  }
  .size-notes li {
    position: relative;
    padding-left: 32px;
    margin-bottom: 16px;
  }
  .size-notes .note-num {
    position: absolute;
    left: 0;
    top: 0;
  }
  .size-table {
    position: absolute;
    left: 94px;
    top: 276px;
    width: 864px;
    height: 350px;
    border-collapse: collapse;
    table-layout: fixed;
    color: var(--ink);
    font-size: 31px;
    font-weight: 400;
    border-top: 3px solid var(--table-edge);
    border-bottom: 3px solid var(--table-edge);
  }
  .size-table td {
    height: 87px;
    padding: 0 0 0 28px;
    vertical-align: middle;
    white-space: nowrap;
  }
  .size-table .col-size { background: var(--col-size); }
  .size-table .col-bust { background: var(--col-bust); }
  .size-table .col-length { background: var(--col-length); }
  .size-table tr + tr td { border-top: 1px solid var(--row-rule); }
</style>
</head>
<body>
  <section class="size-card">
    <svg class="frame-lines" viewBox="0 0 1052 704" aria-hidden="true">
      <g stroke="var(--frame-red)" stroke-width="2.5" fill="none">
        <line x1="0" y1="9" x2="1052" y2="9"/>
        <line x1="0" y1="694" x2="1052" y2="694"/>
        <line x1="10" y1="0" x2="10" y2="704"/>
        <line x1="17" y1="0" x2="17" y2="704"/>
        <line x1="1037" y1="0" x2="1037" y2="704"/>
        <line x1="1044" y1="0" x2="1044" y2="704"/>
      </g>
    </svg>

    <h1 class="size-label">Size Detail (1”=2,54cm)</h1>

    <ol class="size-notes">
      <li><span class="note-num">1.</span>To make sure you get the right size, please refer to our size chart before buying. If you are not sure about size, please email us your exact body measurement, so we can give you some suggestion on how to choose the right size. Thanks for your understanding.</li>
      <li><span class="note-num">2.</span>Manual measurement may have a 1-3cm difference</li>
    </ol>

    <table class="size-table">
      <tbody>
        <tr>
          <td class="col-size">Asian Size: S</td>
          <td class="col-bust">Bust: 80cm/31,5”</td>
          <td class="col-length">Length: 80cm/31,5”</td>
        </tr>
        <tr>
          <td class="col-size">Asian Size: M</td>
          <td class="col-bust">Bust: 84cm/33,1”</td>
          <td class="col-length">Length: 82cm/32,3”</td>
        </tr>
        <tr>
          <td class="col-size">Asian Size: L</td>
          <td class="col-bust">Bust: 88cm/34,6”</td>
          <td class="col-length">Length: 84cm/33,1”</td>
        </tr>
        <tr>
          <td class="col-size">Asian Size: XL</td>
          <td class="col-bust">Bust: 92cm/36,2”</td>
          <td class="col-length">Length: 86cm/33,9”</td>
        </tr>
      </tbody>
    </table>
  </section>
</body>
</html>
```